Lanterne architecture business cards

We are a new company based in New Zealand. We Specialize in High end Luxury Residential Architecture.

Every home is bespoke and is designed to each clients individual requirements and needs.

I like to design buildings that inspire people through light and form while offering a high level of comfort and usability.

Lines of sight, proportion and balance are fundamental to the spaces I create.
Updates

August 5th is current deadline - Today's date is the 13th of August.

Target Market(s)

New Zealanders who want a custom individual home design, typically 30-65 year old males and females

Industry/Entity Type

Architecture

Contact Information for Business Card

Director - Derek Tolson
Contact Number - 0279164073
Email - info@lanternearchitecture-example.co.nz
Webstie - www.lanternearchitecture-example.co.nz
Social Media - @lanternearchitecture

Font styles to use
Sans Serif

Requirements
Must have
• Logo (Both Sides)
Website
Email
Contact Number
Social Media

Nice to have
• Texture
Should not have
• More than 3 colours - typically I would've thought 2 would be good to match the logo.

```html
<!DOCTYPE html>
<html lang="en">
<head>
<meta charset="utf-8">
<title>Lanterne Architecture — Business Cards</title>
<link href="https://fonts.googleapis.com/css2?family=Josefin+Sans:wght@300&display=swap" rel="stylesheet">
<style>
  :root {
    --backdrop: #e4e4e2;
    --card: #1c1c1d;
    --card-pattern: #222223;
    --silver: #c9c9c9;
    --silver-dim: #9a9a9a;
  }
  * { margin: 0; padding: 0; box-sizing: border-box; }
  html, body { width: 1200px; height: 1020px; overflow: hidden; }
  body {
    background: var(--backdrop);
    font-family: "Josefin Sans", "Helvetica Neue", Arial, sans-serif;
    font-weight: 300;
    color: var(--silver);
    position: relative;
  }
  .card {
    position: absolute;
    width: 500px;
    height: 306px;
    background: var(--card);
    border-radius: 3px;
    box-shadow: 0 6px 0 #111, 0 14px 30px rgba(0,0,0,.25);
    overflow: hidden;
  }
  .card--front { left: 80px; top: 170px; }
  .card--back  { left: 620px; top: 500px; }

  .card__pattern {
    position: absolute;
    inset: 0;
    background: var(--card-pattern);
  }

  .wordmark {
    position: absolute;
    text-align: center;
    line-height: 1;
  }
  .wordmark__name {
    display: block;
    font-size: 26px;
    letter-spacing: 11px;
    text-transform: uppercase;
    color: var(--silver);
  }
  .wordmark__sub {
    display: block;
    margin-top: 8px;
    font-size: 8px;
    letter-spacing: 7px;
    text-transform: uppercase;
    color: var(--silver);
  }
  .card--front .wordmark { left: 0; right: 0; top: 128px; }

  .card--back .wordmark { right: 22px; top: 46px; text-align: right; }
  .card--back .wordmark__name { font-size: 18px; letter-spacing: 8px; }
  .card--back .wordmark__sub { font-size: 6px; letter-spacing: 5px; }

  .social-handle {
    position: absolute;
    right: 22px;
    top: 112px;
    font-size: 9px;
    letter-spacing: 1px;
    text-transform: uppercase;
    color: var(--silver-dim);
  }

  .contact {
    position: absolute;
    left: 26px;
    bottom: 26px;
  }
  .contact__name {
    font-size: 20px;
    letter-spacing: 2px;
    text-transform: uppercase;
    color: var(--silver-dim);
    margin-bottom: 10px;
  }
  .contact__list { list-style: none; }
  .contact__item {
    display: flex;
    align-items: center;
    gap: 8px;
    font-size: 10px;
    letter-spacing: .6px;
    text-transform: uppercase;
    color: var(--silver-dim);
    margin-top: 5px;
  }
  .contact__item:first-child { font-size: 14px; letter-spacing: 1.5px; }
  .contact__icon { width: 10px; height: 10px; flex: none; }
</style>
</head>
<body>

  <section class="card card--front" aria-label="Card front">
    <div class="card__pattern" role="img" aria-label="Faint tone-on-tone repeating pattern across the card"></div>
    <div class="wordmark">
      <span class="wordmark__name">Lanterne</span>
      <span class="wordmark__sub">Architecture</span>
    </div>
  </section>

  <section class="card card--back" aria-label="Card back">
    <div class="wordmark">
      <span class="wordmark__name">Lanterne</span>
      <span class="wordmark__sub">Architecture</span>
    </div>

    <p class="social-handle">@lanternearchitecture</p>

    <div class="contact">
      <p class="contact__name">Derek Tolson</p>
      <ul class="contact__list">
        <li class="contact__item">
          <svg class="contact__icon" viewBox="0 0 10 10" aria-hidden="true"><path d="M2 1 L4 1 L4.6 3 L3.4 3.8 Q4.4 5.8 6.2 6.6 L7 5.4 L9 6 L9 8 Q8.6 9 7.4 9 Q1 8 1 2.4 Q1 1.2 2 1 Z" fill="#9a9a9a"/></svg>
          0279164073
        </li>
        <li class="contact__item">
          <svg class="contact__icon" viewBox="0 0 10 10" aria-hidden="true"><rect x="0.5" y="2" width="9" height="6" fill="#9a9a9a"/><path d="M0.5 2 L5 5.5 L9.5 2" fill="none" stroke="#1c1c1d" stroke-width="0.8"/></svg>
          info@lanternearchitecture-example.co.nz
        </li>
        <li class="contact__item">
          <svg class="contact__icon" viewBox="0 0 10 10" aria-hidden="true"><circle cx="5" cy="5" r="4.2" fill="none" stroke="#9a9a9a" stroke-width="0.9"/><ellipse cx="5" cy="5" rx="1.8" ry="4.2" fill="none" stroke="#9a9a9a" stroke-width="0.7"/><line x1="0.8" y1="5" x2="9.2" y2="5" stroke="#9a9a9a" stroke-width="0.7"/></svg>
          www.lanternearchitecture-example.co.nz
        </li>
      </ul>
    </div>
  </section>

</body>
</html>
```